Buisness card

**Front Side:**

**[Your Company Logo]**
**Steadfast Upkeep Engineering**
*Keeping Your Equipment Running Smoothly*

**Contact Information:**
- **Name:** [dale Harwick
- **Title:** [owner
- **Phone:** [5073918246
- **Email:** dale@suevx.com

**Back Side:**

**Services Offered:**
- Routine Inspections
- Equipment Maintenance
- Emergency Repairs
- Consultation Services
- New installs
Tag line
Be proactive not reactive

```html
<!DOCTYPE html>
<html lang="en">
<head>
<meta charset="utf-8">
<title>Steadfast Upkeep Engineering – Business Card</title>
<link rel="stylesheet" href="https://fonts.googleapis.com/css2?family=Roboto:wght@400;700;900&family=Roboto+Condensed:wght@700&display=swap">
<style>
  :root {
    --backdrop: #6fa9c6;
    --paper: #dbeaf5;
    --paper-edge: #c4dcee;
    --navy: #263670;
    --navy-deep: #1d2a5c;
    --band: #1f8ad8;
    --band-light: #56b4f0;
    --sky: #4fb6ee;
    --royal: #1b5fc4;
    --royal-deep: #123f97;
    --white: #ffffff;
    --ink: #141a2e;
    --brand-blue: #1e63c9;
  }
  * { box-sizing: border-box; margin: 0; padding: 0; }
  html, body { width: 1200px; height: 1038px; overflow: hidden; }
  body {
    background: var(--backdrop);
    font-family: "Roboto", Arial, sans-serif;
    position: relative;
  }
  .card {
    position: absolute;
    left: 250px;
    width: 700px;
    height: 400px;
    overflow: hidden;
    box-shadow: 0 10px 24px rgba(20, 50, 80, .35);
  }
  .card--front { top: 90px; background: var(--navy); }
  .card--back { top: 548px; background: linear-gradient(180deg, var(--sky) 0%, var(--royal) 45%, var(--royal-deep) 100%); }

  /* brand lockup */
  .brand { position: absolute; display: flex; align-items: center; }
  .brand__mark { border-radius: 50%; background: var(--navy); flex: none; }
  .brand__name {
    font-weight: 900;
    color: var(--brand-blue);
    line-height: 1.05;
    text-transform: uppercase;
  }
  .brand__slogan { font-weight: 700; color: var(--ink); text-transform: uppercase; letter-spacing: .02em; }

  /* front */
  .front__paper {
    position: absolute; left: 0; top: 0; width: 700px; height: 150px;
    background: var(--paper);
  }
  .front__paper::after {
    content: ""; position: absolute; right: 0; top: 96px; width: 300px; height: 54px;
    background: var(--navy);
    clip-path: polygon(18% 0, 100% 0, 100% 100%, 0 100%);
  }
  .card--front .brand { left: 40px; top: 22px; gap: 20px; }
  .card--front .brand__mark { width: 104px; height: 104px; }
  .card--front .brand__name { font-size: 30px; width: 380px; }
  .card--front .brand__slogan { font-size: 17px; margin-top: 6px; }

  .front__band {
    position: absolute; left: 0; top: 150px; width: 470px; height: 44px;
    background: linear-gradient(90deg, var(--band) 0%, var(--band-light) 100%);
    clip-path: polygon(0 0, 100% 0, 94% 100%, 0 100%);
    display: flex; align-items: center; padding-left: 40px;
  }
  .front__tagline { font-size: 19px; color: var(--navy-deep); font-weight: 400; }

  .person { position: absolute; left: 40px; top: 255px; }
  .person__name { font-size: 30px; font-weight: 700; color: var(--sky); text-transform: capitalize; }
  .person__title { font-size: 17px; color: var(--white); margin-top: 10px; text-transform: uppercase; }

  .contact { position: absolute; left: 410px; top: 170px; color: var(--white); }
  .contact__phone { display: flex; align-items: center; gap: 10px; font-size: 38px; font-weight: 700; }
  .contact__email { display: flex; align-items: center; gap: 10px; font-size: 17px; margin-top: 10px; padding-left: 4px; }
  .contact svg { flex: none; }

  /* back */
  .back__paper {
    position: absolute; left: 0; top: 0; width: 700px; height: 150px;
    background: linear-gradient(180deg, var(--white) 0%, var(--paper) 70%, var(--paper-edge) 100%);
  }
  .card--back .brand { left: 30px; top: 30px; gap: 16px; }
  .card--back .brand__mark { width: 76px; height: 76px; }
  .card--back .brand__name { font-size: 22px; width: 260px; }
  .card--back .brand__slogan { font-size: 12px; margin-top: 4px; }

  .services__heading {
    position: absolute; left: 0; top: 150px; width: 700px; height: 40px;
    background: var(--navy-deep);
    color: var(--white);
    font-family: "Roboto Condensed", Arial, sans-serif;
    font-size: 22px; letter-spacing: .06em;
    display: flex; align-items: center; justify-content: center;
    text-transform: uppercase;
  }
  .services {
    position: absolute; left: 70px; top: 225px;
    display: grid; grid-template-columns: 300px 260px; column-gap: 40px; row-gap: 22px;
    list-style: none;
  }
  .services__item {
    display: flex; align-items: center; gap: 12px;
    font-family: "Roboto Condensed", Arial, sans-serif;
    font-size: 24px; color: var(--white);
    text-shadow: 0 2px 3px rgba(0, 0, 0, .35);
  }
  .services__item svg { flex: none; }
</style>
</head>
<body>

<section class="card card--front" aria-label="Business card front">
  <div class="front__paper"></div>
  <div class="brand">
    <span class="brand__mark"></span>
    <div>
      <p class="brand__name">Steadfast Upkeep Engineering</p>
      <p class="brand__slogan">Be proactive not reactive</p>
    </div>
  </div>
  <div class="front__band"><p class="front__tagline">Keeping Your Equipment Running Smoothly</p></div>

  <div class="person">
    <p class="person__name">dale Harwick</p>
    <p class="person__title">Owner</p>
  </div>

  <div class="contact">
    <p class="contact__phone">
      <svg width="26" height="26" viewBox="0 0 24 24" aria-hidden="true"><path fill="#ffffff" d="M6.6 10.8a15.1 15.1 0 0 0 6.6 6.6l2.2-2.2c.3-.3.7-.4 1-.2 1.1.4 2.3.6 3.6.6.6 0 1 .4 1 1V20c0 .6-.4 1-1 1A17 17 0 0 1 3 4c0-.6.4-1 1-1h3.5c.6 0 1 .4 1 1 0 1.3.2 2.5.6 3.6.1.3 0 .7-.2 1z"/></svg>
      5073-918-246
    </p>
    <p class="contact__email">
      <svg width="18" height="14" viewBox="0 0 18 14" aria-hidden="true"><rect x="1" y="1" width="16" height="12" fill="none" stroke="#ffffff" stroke-width="1.6"/><path d="M1 1l8 7 8-7" fill="none" stroke="#ffffff" stroke-width="1.6"/></svg>
      dale@suevx.com
    </p>
  </div>
</section>

<section class="card card--back" aria-label="Business card back">
  <div class="back__paper"></div>
  <div class="brand">
    <span class="brand__mark"></span>
    <div>
      <p class="brand__name">Steadfast Upkeep Engineering</p>
      <p class="brand__slogan">Be proactive not reactive</p>
    </div>
  </div>
  <h2 class="services__heading">Services Offered</h2>
  <ul class="services">
    <li class="services__item"><svg width="16" height="16" viewBox="0 0 16 16" aria-hidden="true"><path d="M3 3l10 10M13 3L3 13" stroke="#141a2e" stroke-width="3" stroke-linecap="round"/></svg>Routine Inspections</li>
    <li class="services__item"><svg width="16" height="16" viewBox="0 0 16 16" aria-hidden="true"><path d="M3 3l10 10M13 3L3 13" stroke="#141a2e" stroke-width="3" stroke-linecap="round"/></svg>Consultation Services</li>
    <li class="services__item"><svg width="16" height="16" viewBox="0 0 16 16" aria-hidden="true"><path d="M3 3l10 10M13 3L3 13" stroke="#141a2e" stroke-width="3" stroke-linecap="round"/></svg>Equipment Maintenance</li>
    <li class="services__item"><svg width="16" height="16" viewBox="0 0 16 16" aria-hidden="true"><path d="M3 3l10 10M13 3L3 13" stroke="#141a2e" stroke-width="3" stroke-linecap="round"/></svg>New installs</li>
    <li class="services__item"><svg width="16" height="16" viewBox="0 0 16 16" aria-hidden="true"><path d="M3 3l10 10M13 3L3 13" stroke="#141a2e" stroke-width="3" stroke-linecap="round"/></svg>Emergency Repairs</li>
  </ul>
</section>

</body>
</html>
```